Business Cards for a small business advisory (business services)

Professional look. Same as would apply for a lawyer, accountant, or other financial services professional. Please use the logo colors

Target Market(s)

small business owners

Industry/Entity Type

Financial Servics

Contact Information for Business Card

Name: Glenn R. Whitaker, CAIA / Title: Business Advisor / Office #: (555) 284-7193 / Mobile #: (555) 903-6418 / Email: g.whitaker@ambervalebusinessbrokers.example / Web: www.ambervalebusinessbrokers.example

Font styles to use
Sans Serif

```html
<!DOCTYPE html>
<html lang="en">
<head>
<meta charset="utf-8">
<title>Ambervale Business Brokers &amp; Advisors – Business Cards</title>
<link rel="stylesheet" href="https://fonts.googleapis.com/css2?family=Montserrat:wght@400;500;700&display=swap">
<style>
  :root {
    --backdrop: #1b1b1c;
    --card: #2a2a2b;
    --brand-blue: #1f4794;
    --brand-green: #7cc242;
    --text-light: #f1f1f1;
    --emboss-bright: rgba(215, 215, 215, 0.55);
    --emboss-soft: rgba(120, 120, 122, 0.35);
  }
  * { box-sizing: border-box; margin: 0; padding: 0; }
  html, body {
    width: 1200px;
    height: 900px;
    overflow: hidden;
    background: var(--backdrop);
    font-family: "Montserrat", sans-serif;
  }
  .sheet {
    width: 1200px;
    height: 900px;
    display: flex;
    flex-direction: column;
    align-items: center;
    justify-content: center;
    gap: 36px;
  }
  .card {
    position: relative;
    width: 700px;
    height: 400px;
    background: var(--card);
    border-bottom: 8px solid var(--brand-green);
    box-shadow: 0 10px 30px rgba(0, 0, 0, 0.5);
    overflow: hidden;
  }
  .decor {
    position: absolute;
    border-radius: 50%;
  }
  .card-front .decor {
    left: 70px;
    top: 30px;
    width: 320px;
    height: 320px;
    background: radial-gradient(circle at 50% 50%, var(--emboss-bright) 0%, rgba(150, 150, 152, 0.25) 35%, rgba(42, 42, 43, 0) 70%);
  }
  .card-back .decor {
    right: 40px;
    top: 110px;
    width: 330px;
    height: 330px;
    background: radial-gradient(circle at 50% 50%, var(--emboss-soft) 0%, rgba(90, 90, 92, 0.2) 40%, rgba(42, 42, 43, 0) 70%);
  }
  .brand {
    display: flex;
    align-items: center;
    gap: 12px;
  }
  .brand-dot {
    border-radius: 50%;
    background: var(--brand-blue);
    flex: none;
  }
  .brand-name {
    color: var(--brand-blue);
    font-weight: 700;
    letter-spacing: 0.02em;
    line-height: 1.15;
  }

  /* Front */
  .card-front .brand {
    position: absolute;
    right: 44px;
    top: 50%;
    transform: translateY(-50%);
  }
  .card-front .brand-dot { width: 26px; height: 26px; }
  .card-front .brand-name { font-size: 36px; }
  .card-front .brand-name small {
    display: block;
    font-size: 12px;
    letter-spacing: 0.14em;
    text-transform: uppercase;
  }

  /* Back */
  .card-back .brand {
    position: absolute;
    left: 40px;
    top: 34px;
  }
  .card-back .brand-dot { width: 22px; height: 22px; }
  .card-back .brand-name { font-size: 30px; }
  .card-back .brand-name small {
    display: block;
    font-size: 10px;
    letter-spacing: 0.14em;
    text-transform: uppercase;
  }
  .person {
    position: absolute;
    left: 52px;
    top: 182px;
  }
  .person-name {
    font-size: 24px;
    font-weight: 700;
    text-transform: uppercase;
    letter-spacing: 0.03em;
    color: var(--brand-blue);
  }
  .person-name .surname { color: var(--brand-green); }
  .person-title {
    font-size: 16px;
    font-weight: 500;
    color: var(--text-light);
    margin-top: 0;
  }
  .contact-list {
    list-style: none;
    margin-top: 16px;
    font-size: 17px;
    color: var(--text-light);
    line-height: 1.5;
  }
  .contact-list li {
    display: flex;
    align-items: center;
    gap: 8px;
  }
  .contact-list svg {
    width: 14px;
    height: 14px;
    flex: none;
    stroke: var(--brand-green);
    fill: none;
    stroke-width: 2;
  }
</style>
</head>
<body>
<main class="sheet">
  <section class="card card-front" aria-label="Card front">
    <div class="decor" role="img" aria-label="Large embossed decorative emblem area"></div>
    <div class="brand">
      <span class="brand-dot"></span>
      <p class="brand-name">Ambervale<small>Business Brokers &amp; Advisors</small></p>
    </div>
  </section>

  <section class="card card-back" aria-label="Card back">
    <div class="decor" role="img" aria-label="Faint embossed decorative emblem area"></div>
    <div class="brand">
      <span class="brand-dot"></span>
      <p class="brand-name">Ambervale<small>Business Brokers &amp; Advisors</small></p>
    </div>

    <div class="person">
      <h1 class="person-name">Glenn R. <span class="surname">Whitaker, CAIA</span></h1>
      <p class="person-title">Business Advisor</p>
      <ul class="contact-list">
        <li>
          <svg viewBox="0 0 24 24" aria-hidden="true"><path d="M6 3h4l2 5-3 2a11 11 0 0 0 5 5l2-3 5 2v4a2 2 0 0 1-2 2A17 17 0 0 1 4 5a2 2 0 0 1 2-2z"/></svg>
          (555) 284-7193
        </li>
        <li>
          <svg viewBox="0 0 24 24" aria-hidden="true"><rect x="7" y="2" width="10" height="20" rx="2"/><line x1="11" y1="18" x2="13" y2="18"/></svg>
          (555) 903-6418
        </li>
        <li>
          <svg viewBox="0 0 24 24" aria-hidden="true"><rect x="3" y="5" width="18" height="14" rx="1"/><polyline points="3,6 12,13 21,6"/></svg>
          g.whitaker@ambervalebusinessbrokers.example
        </li>
        <li>
          <svg viewBox="0 0 24 24" aria-hidden="true"><circle cx="12" cy="12" r="9"/><line x1="3" y1="12" x2="21" y2="12"/><ellipse cx="12" cy="12" rx="4" ry="9"/></svg>
          www.ambervalebusinessbrokers.example
        </li>
      </ul>
    </div>
  </section>
</main>
</body>
</html>
```